Design Project for Digital Recruitment Business

I am launching a new website in the Digital Marketing Recruitment space here in the UK.We are a start up so this very much phase 1 with our web offering.

Key points:

- I think it will be aproximately 5- 8 pages

- I am looking for wordpress(open on this)) design and coding/ development.

- It really is going to be a brochure site on the whole so don't expect any huge integration. I would like an RSS feed to publish our jobs on our site. I can get the code for that from my recruitment database partner Quillmark, all i will need is a blank page for that section?.Connect Up,chirpnet etc as well.

-I already have the logo.(See attached)which you guys delivered brilliantly on :-)

some reference sites I like the look of: http://www.tavernbright.co.uk http://www.plinthworks.com/ http://www.webmavens.co.uk/

The menu bar on these sites are good, the language is good.I want contemporary and professional.It needs to connect to the viewer.
WE are in the social media space so that needs to fit/blend eg connectup,PB.

SUGGESTED APPROACH
So I guess the best starting point would be to just submit a home page design so i can judge the styles I like best.Then the finalists of that round can submit another section of the website to see the consistency in terms of look and feel. I will then pick someone to work one on one with to complete the design and do the coding. That way no one gets to waste valuable time and energy :-)

Feel free to ping me questions
Updates

Project Deadline Extended
Reason: Hello All, I am going to extend by a few days. I have been inundated with work.However I Plan to look at all your designs this week end and respond to all your Queries. Thanks for your Patience.

Hi guys

here is a little more about us

We know that the career success of the candidates we place can have a great impact on the success of your business. We have built a network of talented industry professionals and an extensive knowledge of the market and its changing trends. We focus on career management,advice and consultancy.With over 30 years experience in our team we feel confident we can deliver. Our specialisms are Creative and Design,Digital Marketing,Editorial and Content,User Experience,and Technology related to building Websites.

In today's world of continually adapting,surviving and thriving we recognise that you rise and fall by the people you hire.That is why an expert  is required to help find those people in business critical roles. So if your online Marketing strategy is behind the times or your website traffic is poor for example we can help find people on a contract and permanent basis to bridge the gap in you marketing and E-commerce team. Online Talentry are specialists in these areas and offer a consultative approach to working with your business. If your business grows as a result of the people you recruited through us we could not be happier. Honest,straightforward,professional.

In terms of home page the Menu bar is 4-5 topics at most. 90% of the traffic to this website will be Candidates so Jobs will be the best content along with the 6 skill sets/categories and everything social after that.Very like Plinth website I mentioned in the Brief. A couple of you are on the right tracks.
Hope this helps for now. I feel confident I can pick from one of you.

Kind regards

Martin

Soory one other thing,

RE; Images

People are tricky to do on Recruitment websites as its very PC and they dont look real enough.Animations of people are better in my humble opinion...

open to ideas/options

Thanks

Target Market(s)

marketeers,designers,ecommerce folks.

Industry/Entity Type

Business

Requirements
Must have
• open at this stage but obviously the logo design colours must sync with the overall look and feel.PB,chirpnet,findr+ must be dominant

```html
<!DOCTYPE html>
<html lang="en">
<head>
<meta charset="utf-8">
<title>Online Talentry – Talented People. Great Careers.</title>
<link rel="stylesheet" href="https://fonts.googleapis.com/css2?family=Montserrat:wght@700;800&family=Noticia+Text&family=Questrial&display=swap">
<style>
  :root {
    --purple: #2c0784;
    --purple-deep: #3a0a9a;
    --orange: #ec6526;
    --orange-light: #f48a3b;
    --pill: #3b0909;
    --text: #555;
    --text-dark: #222;
    --muted: #999;
    --line: #e4e4e4;
    --link: #ef6a2a;
    --tw-blue: #2f8fd8;
    --sq-a: #3b5998;
    --sq-b: #19a9e5;
    --sq-c: #0a6fa6;
    --sq-d: #333;
    --sq-e: #f7892e;
  }
  * { box-sizing: border-box; margin: 0; padding: 0; }
  html, body { width: 960px; height: 1200px; overflow: hidden; background: #fff; }
  body { font-family: "Questrial", sans-serif; color: var(--text); }
  .page { position: relative; width: 960px; height: 1200px; }
  .abs { position: absolute; }
  h1, h2, h3 { font-weight: normal; }

  .social-bar { left: 0; top: 0; width: 960px; height: 38px; background: var(--purple); }
  .social-bar .label { position: absolute; right: 265px; top: 12px; color: #fff; font-size: 11px; letter-spacing: .2px; white-space: nowrap; }
  .squares { position: absolute; display: flex; gap: 8px; }
  .squares span { width: 22px; height: 22px; display: block; }
  .social-bar .squares { left: 704px; top: 7px; }
  .sq-a { background: var(--sq-a); } .sq-b { background: var(--sq-b); }
  .sq-c { background: var(--sq-c); } .sq-d { background: var(--sq-d); }
  .sq-e { background: var(--sq-e); }

  .header { left: 0; top: 38px; width: 960px; height: 66px; background: linear-gradient(#e9e9e9, #fff 70%); }
  .logo { position: absolute; left: 112px; top: 16px; display: flex; align-items: center; gap: 7px;
    font-family: "Montserrat", sans-serif; font-weight: 700; font-size: 24px; color: var(--purple-deep); letter-spacing: -1px; }
  .logo i { width: 26px; height: 26px; border-radius: 50%; background: var(--orange); display: block; }
  .nav { position: absolute; top: 35px; left: 379px; display: flex; font-size: 12px; color: #666; white-space: nowrap; }
  .nav a { color: inherit; text-decoration: none; margin-right: 27px; }
  .nav a.current { background: var(--orange); color: #fff; font-weight: bold; padding: 3px 8px; border-radius: 7px; margin-top: -4px; height: 20px; margin-right: 23px; }
  .nav a:last-child { margin-right: 0; }
  .rule { left: 112px; top: 104px; width: 734px; height: 1px; background: var(--line); }

  .people { left: 140px; top: 112px; width: 290px; height: 215px; border-radius: 80px 80px 0 0;
    background: linear-gradient(90deg, #6d7488, #c9c9cc 50%, #8d8b86); }
  .tagline { left: 440px; top: 150px; width: 404px; text-align: right; white-space: nowrap; font-family: "Noticia Text", serif; font-size: 26px; color: #111; letter-spacing: .3px; }
  .search { left: 455px; top: 205px; width: 381px; height: 40px; border: 1px solid #ccc; border-radius: 4px;
    background: linear-gradient(#f2f2f2, #fff); box-shadow: inset 0 1px 3px rgba(0,0,0,.15); }
  .search .placeholder { position: absolute; left: 10px; top: 7px; font-family: "Noticia Text", serif; font-style: italic; font-size: 19px; color: var(--purple); white-space: nowrap; }
  .search .btn { position: absolute; right: 2px; top: 3px; width: 82px; height: 33px; background: var(--purple); color: #fff;
    border-radius: 4px; font-family: "Noticia Text", serif; font-size: 19px; text-align: center; line-height: 33px; }

  .banner { left: 0; top: 0; }
  .banner-title { left: 115px; top: 342px; width: 729px; text-align: center; color: #fff; font-size: 25px; font-weight: normal; }
  .banner-sub { left: 115px; top: 379px; width: 729px; text-align: center; color: #fff; font-family: "Noticia Text", serif; font-size: 18px; }
  .areas { left: 140px; width: 680px; display: flex; justify-content: center; gap: 11px; white-space: nowrap; }
  .areas span { background: var(--pill); color: #fff; font-size: 12px; height: 25px; line-height: 25px; padding: 0 13px; border-radius: 13px; }

  .section-title { top: 560px; width: 260px; text-align: center; font-family: "Montserrat", sans-serif; font-weight: 800; font-size: 30px; letter-spacing: -1.5px; }
  .section-title b { color: var(--purple-deep); font-weight: 800; }
  .section-title em { color: var(--orange); font-style: normal; }
  .card { top: 627px; width: 198px; height: 255px; background: #fff; border: 1px solid #eee; border-radius: 6px; box-shadow: 0 1px 4px rgba(0,0,0,.12); }
  .card .clip { position: absolute; left: 94px; top: -18px; width: 10px; height: 30px; background: linear-gradient(90deg,#ddd,#fff,#ccc); border-radius: 3px; }
  .card .hole { position: absolute; left: 62px; top: 15px; width: 74px; height: 11px; border: 1px solid #ccc; border-radius: 6px; }
  .card .photo { position: absolute; left: 16px; top: 44px; width: 166px; height: 86px; border-radius: 6px; }
  .card p { position: absolute; left: 16px; top: 143px; width: 166px; text-align: center; font-size: 11.5px; line-height: 16.5px; color: #666; }

  .tweets { left: 0; top: 930px; width: 960px; height: 85px; background: linear-gradient(#fff, #eee); border-top: 1px solid #eee; border-bottom: 2px solid #ddd; }
  .tweets .handle { position: absolute; left: 0; top: 15px; width: 960px; text-align: center; font-size: 10px; color: var(--tw-blue); }
  .tweets .msg { position: absolute; left: 189px; top: 35px; font-size: 12px; color: #555; white-space: nowrap; }
  .tweets .msg a { color: var(--link); text-decoration: none; }
  .tweets .bird { position: absolute; left: 156px; top: 32px; }
  .tweets .time { position: absolute; left: 0; top: 56px; width: 960px; text-align: center; font-size: 8px; color: var(--muted); }
  .tweets .dots { position: absolute; top: 72px; left: 471px; display: flex; gap: 3px; }
  .tweets .dots i { width: 3px; height: 3px; border-radius: 50%; background: #bbb; display: block; }
  .tweets .dots i:first-child { background: var(--tw-blue); }

  .footer-col { top: 1036px; font-size: 11px; color: #555; line-height: 15px; }
  .footer-col h3 { font-size: 12px; color: var(--text-dark); margin-bottom: 12px; letter-spacing: .2px; font-weight: bold; }
  .footer-col .country { color: #a0262a; font-size: 11px; }
  .footer-col .org { color: #333; font-weight: bold; margin-bottom: 4px; }
  .links { display: grid; grid-template-columns: 82px 80px; row-gap: 4px; padding-left: 2px; }
  .footer-col .squares { position: static; }
  .copyright { left: 0; top: 1163px; width: 960px; height: 37px; background: var(--purple); color: #b7a8e8; font-size: 11px; text-align: center; line-height: 35px; }
</style>
</head>
<body>
<div class="page">

  <div class="abs social-bar">
    <span class="label">LET' S GET SOCIAL</span>
    <div class="squares" aria-label="Social profiles">
      <span class="sq-a" title="PB"></span><span class="sq-b" title="chirpnet"></span><span class="sq-c" title="Connect Up"></span><span class="sq-d" title="findr+"></span><span class="sq-e" title="RSS"></span>
    </div>
  </div>

  <header class="abs header">
    <div class="logo"><i></i>onlinetalentry</div>
    <nav class="nav">
      <a class="current" href="#">home</a><a href="#">clients</a><a href="#">candidates</a><a href="#">jobs</a><a href="#">about us</a><a href="#">resources</a><a href="#">contact</a>
    </nav>
  </header>
  <div class="abs rule"></div>

  <div class="abs people" role="img" aria-label="Smiling young man and woman, candidates"></div>
  <h1 class="abs tagline">Talented People. Great Careers.</h1>
  <div class="abs search">
    <span class="placeholder">Search for your perfect job...</span>
    <span class="btn">Search</span>
  </div>

  <svg class="abs banner" width="960" height="580" viewBox="0 0 960 580" aria-hidden="true">
    <defs>
      <linearGradient id="bannerFill" x1="0" y1="0" x2="1" y2="1">
        <stop offset="0" stop-color="#e85c25"/><stop offset="1" stop-color="#f58d3c"/>
      </linearGradient>
      <radialGradient id="bannerShadow" cx="0.5" cy="0.5" r="0.5">
        <stop offset="0" stop-color="#000" stop-opacity=".18"/><stop offset="1" stop-color="#000" stop-opacity="0"/>
      </radialGradient>
    </defs>
    <ellipse cx="480" cy="540" rx="380" ry="22" fill="url(#bannerShadow)"/>
    <path d="M127,303 Q480,348 832,302 Q845,301 845,315 L845,521 Q845,535 831,535 Q480,498 129,535 Q115,535 115,521 L115,318 Q115,303 127,303 Z"
          fill="url(#bannerFill)" stroke="#7a3410" stroke-width="3"/>
  </svg>
  <h2 class="abs banner-title">Taking a personal approach to digital recruitment</h2>
  <p class="abs banner-sub">Areas we cover:</p>
  <div class="abs areas" style="top:419px">
    <span>Ad tech &amp; Sales</span><span>Client Services</span><span>Digital Marketing</span><span>Creative &amp; Design</span><span>Strategy &amp; Planning</span>
  </div>
  <div class="abs areas" style="top:456px">
    <span>Technology</span><span>Search Marketing</span><span>Mobile</span><span>Project Management</span><span>Social Media</span>
  </div>

  <h2 class="abs section-title" style="left:90px"><b>dream</b><em>jobs</em></h2>
  <h2 class="abs section-title" style="left:346px"><b>dream</b><em>hire</em></h2>
  <h2 class="abs section-title" style="left:613px"><b>join</b><em>us</em></h2>

  <article class="abs card" style="left:121px">
    <span class="hole"></span><span class="clip"></span>
    <div class="photo" role="img" aria-label="Person holding a sign saying they love their job" style="background:linear-gradient(90deg,#7a3fb0,#d8b27a 50%,#7a3fb0)"></div>
    <p>Lorem Ipsum is simply dummy text of the printing and typesetting industry. Lorem Ipsum has been the industry's standard dummy text ever since the 1500s.</p>
  </article>
  <article class="abs card" style="left:380px">
    <span class="hole"></span><span class="clip"></span>
    <div class="photo" role="img" aria-label="Business people shaking hands in a meeting" style="background:linear-gradient(90deg,#e9dccb,#a8b4c4 55%,#d7d9dc)"></div>
    <p>Lorem Ipsum is simply dummy text of the printing and typesetting industry. Lorem Ipsum has been the industry's standard dummy text ever since the 1500s.</p>
  </article>
  <article class="abs card" style="left:638px">
    <span class="hole"></span><span class="clip"></span>
    <div class="photo" role="img" aria-label="Team joining hands in a high five" style="background:linear-gradient(90deg,#c9d6e4,#e2c9b4 50%,#9fb3c8)"></div>
    <p>Lorem Ipsum is simply dummy text of the printing and typesetting industry. Lorem Ipsum has been the industry's standard dummy text ever since the 1500s.</p>
  </article>

  <section class="abs tweets">
    <span class="handle">@talentrydesk</span>
    <svg class="bird" width="26" height="22" viewBox="0 0 26 22" aria-hidden="true"><ellipse cx="13" cy="12" rx="11" ry="8" fill="var(--tw-blue)"/></svg>
    <span class="msg">Lorem ipsum dolor sit amet, consectetur adipisicing elit, sed do eiusmod. check it out at <a href="#">http://tl.ink/Rq4pW8a</a></span>
    <span class="time">about 17 hours, 25 minutes ago</span>
    <span class="dots"><i></i><i></i><i></i></span>
  </section>

  <footer>
    <div class="abs footer-col" style="left:112px">
      <h3>CONTACT US</h3>
      <div class="country">COUNTRY NAME</div>
      <div class="org">Online Talentry</div>
      <div>Telephone : +11 (1)2 555 0148</div>
      <div>Fax : +11 (1)2 555 0148</div>
      <div>Email : info@onlinetalentry.com</div>
    </div>
    <div class="abs footer-col" style="left:412px">
      <h3>QUICK LINKS</h3>
      <div class="links">
        <span>Home</span><span>About us</span><span>Clients</span><span>Resources</span><span>Candidates</span><span>Contact</span><span>Jobs</span>
      </div>
    </div>
    <div class="abs footer-col" style="left:702px">
      <h3>CONNECT WITH US</h3>
      <div class="squares" aria-label="Social profiles">
        <span class="sq-a" title="PB"></span><span class="sq-b" title="chirpnet"></span><span class="sq-c" title="Connect Up"></span><span class="sq-d" title="findr+"></span><span class="sq-e" title="RSS"></span>
      </div>
    </div>
    <div class="abs copyright">Copyright © 2012 The Online Talentry.&nbsp; All rights reserved.</div>
  </footer>

</div>
</body>
</html>
```